Ancient Art and Artifact information website

Hello Designers,
We are starting up a new website who talk abut and discusses an ancient arts artifacts. We would covering a wide range of countries ranging from Egypt, Greece, India, Syria, Rome, etc. My website name Brisk Loom
Designs that fits with ancient theme and some kind of uniqueness would be accepted.
Requirements:
1) A home page design
2) Sub page design
3) A suitable logo
Sections can be added are featured ancient arts/places with short description followed by a more button, latest news, and comment section.
Add contents if you found relevant for this category of website. Ability to share the information through social media is desired.
Must be a responsive design. I look forward to designs which are mind blowing.
2 page

```html
<!DOCTYPE html>
<html lang="en">
<head>
<meta charset="utf-8">
<title>Brisk Loom — Ancient Art</title>
<link rel="stylesheet" href="https://fonts.googleapis.com/css2?family=Oswald:wght@300;400;500&display=swap">
<style>
:root{
  --ink:#1d1d1d;
  --red:#c4161c;
  --bar:#232323;
  --paper:#f7f6f3;
  --line:#cfcfcf;
  --muted:#6b6b6b;
}
*{margin:0;padding:0;box-sizing:border-box}
html,body{width:1200px;height:4972px;overflow:hidden}
body{position:relative;background:var(--paper);font-family:'Oswald',sans-serif;color:var(--ink)}
.abs{position:absolute}
.site-header{left:0;top:0;width:1200px;height:176px;background:#fff}
.brand{left:0;width:1200px;text-align:center;font-size:76px;line-height:1;font-weight:400;letter-spacing:1px;color:var(--ink)}
.site-header .brand{top:56px}
.main-nav{left:0;top:176px;width:1200px;height:83px;background:var(--bar);display:flex;justify-content:center;gap:52px;align-items:center}
.main-nav a{color:#fff;text-decoration:none;font-size:19px;position:relative;padding:10px 0}
.main-nav a.active::after{content:"";position:absolute;left:0;right:0;bottom:-4px;height:3px;background:var(--red)}
.hero{left:0;top:259px;width:1200px;height:693px;background:linear-gradient(90deg,#1a1d24 0%,#2a2d33 40%,#3a3836 100%)}
.hero-figure{left:430px;top:0;width:770px;height:693px;background:radial-gradient(ellipse at 55% 45%,#8a6a3a 0%,#4a3a26 40%,rgba(40,38,40,0) 72%)}
.hero-title{left:190px;top:160px;font-size:88px;line-height:88px;font-weight:400;color:#fff}
.hero-title span{color:var(--red);display:block}
.btn-outline{border:2px solid #fff;color:#fff;font-size:20px;text-align:center}
.hero .btn-outline{left:189px;top:477px;width:179px;height:56px;line-height:52px}
.hero-arrow{width:52px;height:52px;border:2px solid #fff;border-radius:50%;top:312px}
.band{left:205px;width:790px;height:20px;background:linear-gradient(#555,#888);opacity:.75}
.section-title{left:0;width:1200px;text-align:center;color:var(--red);font-size:28px;line-height:40px;font-weight:400}
.feature-img{left:202px;width:385px;height:252px}
.img-label{left:20px;bottom:14px;color:#fff;font-size:21px}
.feature-text{left:617px;width:380px}
.posted{font-size:15px;color:var(--ink)}
.feature-title{margin-top:8px;font-size:24px;line-height:32px}
.btn-small{display:block;margin-top:16px;width:86px;height:28px;border:2px solid var(--ink);font-size:13px;text-align:center;line-height:24px}
.btn-dark{border:2px solid var(--ink);font-size:19px;text-align:center}
.place-img{width:252px;height:182px}
.place-name{width:252px;text-align:center;font-size:22px}
.news-img{width:216px;height:202px}
.news-tag{left:10px;top:0;width:56px;height:60px;background:var(--red);color:#fff;font-size:9px;text-align:center;padding-top:8px}
.news-tag b{display:block;font-size:20px;font-weight:400}
.news-text{width:216px;font-size:13px;line-height:17px}
.news-more{width:86px;height:26px;border:2px solid var(--ink);font-size:11px;text-align:center;line-height:22px}
.comments-title{left:202px;top:3548px;font-size:30px;font-weight:500}
.comment-box{left:202px;top:3613px;width:796px;height:200px;background:#fff;border:1px solid #eee}
.btn-send{left:202px;top:3849px;width:146px;height:49px;background:var(--red);color:#fff;font-size:25px;text-align:center;line-height:49px}
.avatar{left:238px;width:113px;height:113px;border-radius:50%}
.comment{left:375px;width:596px}
.comment-name{font-size:16px}
.comment-views{position:absolute;right:0;top:0;font-size:12px;color:var(--ink)}
.comment-views::before{content:"";display:inline-block;width:14px;height:8px;background:var(--red);border-radius:50%;margin-right:6px}
.comment-body{margin-top:12px;font-size:13px;line-height:20px;color:var(--muted);font-weight:300}
.comment-actions{margin-top:12px;font-size:13px;color:var(--muted)}
.site-footer{left:0;top:4707px;width:1200px;height:265px;background:var(--bar)}
.site-footer .brand{top:52px;color:#fff;font-size:70px}
.social{left:0;top:142px;width:1200px;display:flex;justify-content:center;gap:12px}
.social span{width:34px;height:34px;border:2px solid #fff;border-radius:50%}
.copyright{left:0;top:192px;width:1200px;text-align:center;color:#fff;font-size:14px;line-height:20px}
</style>
</head>
<body>

<header class="abs site-header"><div class="abs brand">BRISK LOOM</div></header>
<nav class="abs main-nav">
  <a class="active">HOME</a><a>ABOUT</a><a>FEATURED ARTS</a><a>PLACES</a><a>LATEST NEWS</a><a>CONTACT US</a>
</nav>

<section class="abs hero">
  <div class="abs hero-figure" role="img" aria-label="Golden pharaoh statue bust"></div>
  <h1 class="abs hero-title">EGYPT<span>ANCIENT</span>ART</h1>
  <div class="abs btn-outline">LEARN MORE</div>
  <svg class="abs hero-arrow" style="left:67px" viewBox="0 0 52 52"><path d="M30 16 L20 26 L30 36" fill="none" stroke="#fff" stroke-width="3"/></svg>
  <svg class="abs hero-arrow" style="left:1081px" viewBox="0 0 52 52"><path d="M22 16 L32 26 L22 36" fill="none" stroke="#fff" stroke-width="3"/></svg>
</section>

<div class="abs band" role="img" aria-label="Zigzag ornament band" style="top:1032px"></div>
<h2 class="abs section-title" style="top:1061px">FEATURED ANCIENT ARTS</h2>
<div class="abs band" role="img" aria-label="Zigzag ornament band" style="top:1110px"></div>

<div class="abs feature-img" role="img" aria-label="Red carved Buddha sculpture" style="top:1207px;background:linear-gradient(135deg,#8a2a14,#c0542a,#5a1a0c)"><span class="abs img-label">INDIA</span></div>
<div class="abs feature-text" style="top:1242px"><div class="posted">POSTED ON MARCH 8 | 2017</div><div class="feature-title">SED UT PERSPICIATIS UNDE OMNIS ISTE NATUS ERROR SIT VOLUPTATEM ACCUSANTIUM DOLOREMQUE</div><span class="btn-small">MORE</span></div>

<div class="abs feature-img" role="img" aria-label="Egyptian painted wall relief" style="top:1492px;background:linear-gradient(135deg,#6a4a2a,#9c7a4a,#3a4a5a)"><span class="abs img-label">EGYPT</span></div>
<div class="abs feature-text" style="top:1527px"><div class="posted">POSTED ON MARCH 8 | 2017</div><div class="feature-title">SED UT PERSPICIATIS UNDE OMNIS ISTE NATUS ERROR SIT VOLUPTATEM ACCUSANTIUM DOLOREMQUE</div><span class="btn-small">MORE</span></div>

<div class="abs feature-img" role="img" aria-label="Greek rock ruins under blue sky" style="top:1777px;background:linear-gradient(180deg,#7aa0c8,#8a8060 55%,#5a6a3a)"><span class="abs img-label">GREECE</span></div>
<div class="abs feature-text" style="top:1812px"><div class="posted">POSTED ON MARCH 8 | 2017</div><div class="feature-title">SED UT PERSPICIATIS UNDE OMNIS ISTE NATUS ERROR SIT VOLUPTATEM ACCUSANTIUM DOLOREMQUE</div><span class="btn-small">MORE</span></div>

<div class="abs btn-dark" style="left:504px;top:2102px;width:189px;height:46px;line-height:42px">VIEW MORE ARTS</div>

<div class="abs band" role="img" aria-label="Zigzag ornament band" style="top:2244px"></div>
<h2 class="abs section-title" style="top:2271px">OUR PLACES</h2>
<div class="abs band" role="img" aria-label="Zigzag ornament band" style="top:2318px"></div>

<div class="abs place-img" role="img" aria-label="India Gate monument" style="left:202px;top:2390px;background:linear-gradient(180deg,#c9d8e2,#b89a6a)"></div>
<div class="abs place-img" role="img" aria-label="Greek island village by the sea" style="left:474px;top:2390px;background:linear-gradient(180deg,#e0a060,#f0e8e0 55%,#2a5a8a)"></div>
<div class="abs place-img" role="img" aria-label="Egyptian pyramids in the desert" style="left:746px;top:2390px;background:linear-gradient(180deg,#e8c890,#c89050)"></div>
<div class="abs place-name" style="left:202px;top:2590px">INDIA</div>
<div class="abs place-name" style="left:474px;top:2590px">GREECE</div>
<div class="abs place-name" style="left:746px;top:2590px">EGYPT</div>

<div class="abs place-img" role="img" aria-label="Syrian ruins at sunset" style="left:202px;top:2655px;background:linear-gradient(180deg,#e07a20,#8a3a10 70%,#2a1a10)"></div>
<div class="abs place-img" role="img" aria-label="Roman forum ruins" style="left:474px;top:2655px;background:linear-gradient(180deg,#7a9ac0,#a08a6a 60%,#5a4a3a)"></div>
<div class="abs place-img" role="img" aria-label="Great Wall of China over hills" style="left:746px;top:2655px;background:linear-gradient(180deg,#d8b070,#6a6a3a 60%,#3a4a2a)"></div>
<div class="abs place-name" style="left:202px;top:2855px">SYRIA</div>
<div class="abs place-name" style="left:474px;top:2855px">ROME</div>
<div class="abs place-name" style="left:746px;top:2855px">CHINA</div>

<div class="abs band" role="img" aria-label="Zigzag ornament band" style="top:2970px"></div>
<h2 class="abs section-title" style="top:2998px">LATEST NEWS</h2>
<div class="abs band" role="img" aria-label="Zigzag ornament band" style="top:3044px"></div>
<svg class="abs" style="left:200px;top:3008px" width="16" height="24" viewBox="0 0 16 24"><path d="M12 3 L4 12 L12 21" fill="none" stroke="#1d1d1d" stroke-width="3"/></svg>
<svg class="abs" style="left:982px;top:3008px" width="16" height="24" viewBox="0 0 16 24"><path d="M4 3 L12 12 L4 21" fill="none" stroke="#1d1d1d" stroke-width="3"/></svg>

<div class="abs news-img" role="img" aria-label="Prehistoric red cave painting" style="left:219px;top:3126px;background:linear-gradient(135deg,#d8c0a0,#b89070)"><div class="abs news-tag">MARCH 8<b>2017</b></div></div>
<div class="abs news-img" role="img" aria-label="Colourful tribal pattern artwork" style="left:491px;top:3126px;background:linear-gradient(135deg,#2a1a10,#8a5a2a,#1a1a1a)"><div class="abs news-tag">MARCH 8<b>2017</b></div></div>
<div class="abs news-img" role="img" aria-label="Ancient stone doorway with light" style="left:762px;top:3126px;background:radial-gradient(ellipse at 50% 45%,#e8c080,#7a4a20 50%,#2a1a10)"><div class="abs news-tag">MARCH 8<b>2017</b></div></div>
<div class="abs news-text" style="left:219px;top:3352px">SED UT PERSPICIATIS UNDE OMNIS ISTE NATUS ERROR SIT...</div>
<div class="abs news-text" style="left:491px;top:3352px">SED UT PERSPICIATIS UNDE OMNIS ISTE NATUS ERROR SIT...</div>
<div class="abs news-text" style="left:762px;top:3352px">SED UT PERSPICIATIS UNDE OMNIS ISTE NATUS ERROR SIT...</div>
<div class="abs news-more" style="left:219px;top:3408px">READ MORE</div>
<div class="abs news-more" style="left:491px;top:3408px">READ MORE</div>
<div class="abs news-more" style="left:762px;top:3408px">READ MORE</div>

<h2 class="abs comments-title">COMMENTS</h2>
<div class="abs comment-box"></div>
<div class="abs btn-send">SEND</div>

<div class="abs avatar" role="img" aria-label="Reader portrait" style="top:4008px;background:#8a7a6a"></div>
<div class="abs comment" style="top:4014px"><div class="comment-name">AREN HALLOWAY</div><span class="comment-views">1,202 VIEWS</span><p class="comment-body">Sed ut perspiciatis unde omnis iste natus error sit voluptatem accusantium doloremque laudantium, totam rem aperiam, eaque ipsa quae ab illo inventore veritatis et.</p><div class="comment-actions">Reply &nbsp;|&nbsp; Like</div></div>

<div class="abs avatar" role="img" aria-label="Reader portrait" style="top:4220px;background:#b0aaa4"></div>
<div class="abs comment" style="top:4226px"><div class="comment-name">MILO STENRICK</div><span class="comment-views">1,202 VIEWS</span><p class="comment-body">Sed ut perspiciatis unde omnis iste natus error sit voluptatem accusantium doloremque laudantium, totam rem aperiam, eaque ipsa quae ab illo inventore veritatis et.</p><div class="comment-actions">Reply &nbsp;|&nbsp; Like</div></div>

<div class="abs avatar" role="img" aria-label="Reader portrait" style="top:4436px;background:#4a6a7a"></div>
<div class="abs comment" style="top:4442px"><div class="comment-name">JUNA PERROW</div><span class="comment-views">1,202 VIEWS</span><p class="comment-body">Sed ut perspiciatis unde omnis iste natus error sit voluptatem accusantium doloremque laudantium, totam rem aperiam, eaque ipsa quae ab illo inventore veritatis et.</p><div class="comment-actions">Reply &nbsp;|&nbsp; Like</div></div>

<footer class="abs site-footer">
  <div class="abs brand">BRISK LOOM</div>
  <div class="abs social"><span></span><span></span><span></span><span></span><span></span></div>
  <div class="abs copyright">© 2017 COMPANY NAME &nbsp;|&nbsp; ALL RIGHTS RESERVED</div>
</footer>

</body>
</html>
```